Building / construction Bussiness card design

I need a new design and logo for my company LWT I am a builder who can project manage or design and construct any kind of building, Residential, Commercial and industrial construction.

On the face side of the card I would like to have just the logo.

Industry/Entity Type

Construction

Contact Information for Business Card

LWT Lakeside Works Team
ABN:84 392 017 655
Carl Moretti
Licenced Builders
0471 926 054
carl@lakesideworksteam.com.au
PO Box 482 Tallowmere BC 2739

```html
<!DOCTYPE html>
<html lang="en">
<head>
<meta charset="utf-8">
<title>Lakeside Works Team – Business Card</title>
<link rel="stylesheet" href="https://fonts.googleapis.com/css2?family=Open+Sans:wght@400;600;700&display=swap">
<style>
  :root {
    --backdrop: #e6e7e8;
    --backdrop-edge: #d9dadb;
    --card-edge: #2b2b2b;
    --face-light: #f2f2f3;
    --face-dark: #c9cacc;
    --brand-blue: #0fa3e0;
    --band-cyan: #00b3ec;
    --ink: #1a1a1a;
    --icon-red: #a3161b;
    --white: #ffffff;
  }
  * { box-sizing: border-box; margin: 0; padding: 0; }
  html, body { width: 1200px; height: 1200px; overflow: hidden; }
  body {
    position: relative;
    font-family: "Open Sans", Arial, sans-serif;
    background: radial-gradient(circle at 50% 50%, #f1f2f2 0%, var(--backdrop) 60%, var(--backdrop-edge) 100%);
    border: 2px solid #555;
  }
  .card {
    position: absolute;
    left: 220px;
    width: 763px;
    height: 461px;
    border: 1.5px solid var(--card-edge);
    border-radius: 0 36px 0 36px;
    overflow: hidden;
  }
  .card--front {
    top: 128px;
    background: radial-gradient(ellipse 60% 65% at 50% 52%, var(--white) 0%, var(--face-light) 35%, var(--face-dark) 100%);
  }
  .card--back {
    top: 601px;
    background: linear-gradient(90deg, #bfc0c2 0%, #e4e5e6 4%, #fbfbfb 10%, var(--white) 14%, var(--white) 100%);
  }
  .abn-band {
    position: absolute;
    right: 0;
    bottom: 0;
    width: 287px;
    height: 47px;
    background: var(--band-cyan);
    color: var(--white);
    font-weight: 600;
    font-size: 18px;
    line-height: 47px;
    padding-left: 58px;
    letter-spacing: 0.2px;
  }
  .wordmark {
    position: absolute;
    left: 0;
    right: 0;
    top: 118px;
    text-align: center;
    color: var(--brand-blue);
    font-weight: 700;
  }
  .wordmark__initials { display: block; font-size: 118px; line-height: 1; letter-spacing: 4px; }
  .wordmark__name { display: block; font-size: 50px; line-height: 1.1; margin-top: 6px; }
  .back-mark {
    position: absolute;
    left: 70px;
    top: 42px;
    color: var(--brand-blue);
    font-weight: 700;
    font-size: 76px;
    line-height: 1;
    letter-spacing: 3px;
  }
  .holder {
    position: absolute;
    left: 533px;
    top: 148px;
    color: var(--ink);
  }
  .holder__name { font-weight: 600; font-size: 21px; line-height: 1.2; }
  .holder__role { font-size: 17px; line-height: 1.3; }
  .contact-list {
    position: absolute;
    left: 45px;
    top: 278px;
    list-style: none;
    color: var(--ink);
    font-size: 17px;
  }
  .contact-list li {
    display: flex;
    align-items: center;
    height: 24.5px;
  }
  .contact-icon { width: 22px; height: 22px; margin-right: 9px; flex: none; }
</style>
</head>
<body>

  <section class="card card--front" aria-label="Card front">
    <div class="wordmark">
      <span class="wordmark__initials">LWT</span>
      <span class="wordmark__name">Lakeside Works Team</span>
    </div>
    <div class="abn-band">ABN: 84 392 017 655</div>
  </section>

  <section class="card card--back" aria-label="Card back">
    <div class="back-mark">LWT</div>

    <div class="holder">
      <p class="holder__name">Carl Moretti</p>
      <p class="holder__role">Licenced Builders</p>
    </div>

    <ul class="contact-list">
      <li>
        <svg class="contact-icon" viewBox="0 0 22 22" aria-hidden="true">
          <circle cx="11" cy="11" r="11" fill="#fff"/>
          <rect x="7" y="3.5" width="8" height="15" rx="1.5" fill="var(--icon-red)"/>
          <rect x="8.3" y="5" width="5.4" height="4.5" fill="#fff"/>
          <rect x="8.3" y="11" width="5.4" height="5.5" fill="#e8b4b6"/>
        </svg>
        0471 926 054
      </li>
      <li>
        <svg class="contact-icon" viewBox="0 0 22 22" aria-hidden="true">
          <circle cx="11" cy="11" r="11" fill="#fff"/>
          <rect x="3" y="6" width="16" height="11" fill="var(--icon-red)"/>
          <path d="M3 6 L11 12.5 L19 6" fill="none" stroke="#fff" stroke-width="1.3"/>
        </svg>
        carl@lakesideworksteam.com.au
      </li>
      <li>
        <svg class="contact-icon" viewBox="0 0 22 22" aria-hidden="true">
          <circle cx="11" cy="11" r="11" fill="#fff"/>
          <path d="M2.5 11.5 L11 4 L19.5 11.5 L17.5 11.5 L17.5 18 L4.5 18 L4.5 11.5 Z" fill="var(--icon-red)"/>
          <rect x="9" y="13" width="4" height="5" fill="#fff"/>
        </svg>
        PO Box 482 Tallowmere BC 2739
      </li>
    </ul>

    <div class="abn-band">ABN: 84 392 017 655</div>
  </section>

</body>
</html>
```